Business Card & Stationary
Powder Coating Company
Project: Business Card & Stationary
Business Card & Stationary - Miscellaneous
Creative Brief
Professional
Rutger Vandelow
Owner / Operator
4715 Ave K 1/2
nullemail@brindlecoatfinish.com
www.brindlecoatfinish.com
Should list our services, which include Powder Coating, Ceramic Coating and Abrasive Blasting

```html
<!DOCTYPE html>
<html lang="en">
<head>
<meta charset="utf-8">
<title>Brindlecoat Finish – Stationery Set</title>
<link href="https://fonts.googleapis.com/css2?family=Roboto+Condensed:wght@400;700&display=swap" rel="stylesheet">
<style>
:root{
  --bg:#e9e6e2;
  --paper:#ffffff;
  --red:#d3202d;
  --red-dark:#9e1520;
  --grey:#8a8a8a;
  --ink:#333333;
  --black:#1c1c1c;
}
*{box-sizing:border-box;margin:0;padding:0}
html,body{width:1200px;height:310px;overflow:hidden;background:var(--bg);font-family:"Roboto Condensed",Arial,sans-serif;color:var(--ink)}
.canvas{position:relative;width:1200px;height:310px}
.piece{position:absolute;background:var(--paper);box-shadow:0 2px 5px rgba(0,0,0,.25);overflow:hidden}
.swoosh{position:absolute;left:0;bottom:0;width:100%;display:block}
.brand{display:flex;align-items:center;gap:4px;font-weight:700;color:var(--red);white-space:nowrap;line-height:1}
.brand .dot{width:.8em;height:.8em;border-radius:50%;background:var(--red);flex:none}
.brand.on-red{color:var(--paper)}
.brand.on-red .dot{background:var(--paper)}
.tiny{font-size:5px;line-height:1.35;color:var(--ink)}
.mark{position:absolute;left:12px;top:8px;font-size:22px}
.mark-tag{position:absolute;left:38px;top:34px;font-size:8px;color:var(--grey)}
.card{width:106px;height:60px}
.card-info .brand{position:absolute;left:6px;top:6px;font-size:9px}
.card-info .who{position:absolute;left:6px;top:22px}
.card-info .who b{display:block;font-size:6px;color:var(--black)}
.card-info .where{position:absolute;right:6px;top:22px;text-align:right}
.card-front .brand,
.card-red .brand{position:absolute;left:0;right:0;justify-content:center;font-size:9px}
.card-front .brand{top:20px}
.card-red .brand{top:25px}
.card-front .services{position:absolute;left:0;right:0;bottom:5px;text-align:center;font-size:4px;color:var(--grey)}
.card-red{background:var(--red)}
.letter{width:186px;height:282px}
.letter .brand{position:absolute;left:14px;top:18px;font-size:13px}
.letter .contact{position:absolute;right:14px;top:16px;text-align:right}
.letter .foot{position:absolute;left:0;right:0;bottom:4px;text-align:center;font-size:4px;color:var(--paper)}
.env{width:156px}
.env .brand{position:absolute;left:8px;top:8px;font-size:9px}
.env .return{position:absolute;left:8px;top:20px}
.dl{width:305px}
.dl .flap{position:absolute;left:0;top:0;width:100%;height:100%;display:block}
.dl .brand{position:absolute;left:50%;transform:translateX(-50%);font-size:10px}
</style>
</head>
<body>
<main class="canvas">

  <div class="brand mark"><span class="dot"></span>Brindlecoat Finish</div>
  <div class="mark-tag">Powder Coating Company</div>

  <!-- business card: details side -->
  <section class="piece card card-info" style="left:14px;top:173px">
    <div class="brand"><span class="dot"></span>Brindlecoat Finish</div>
    <div class="who tiny"><b>Rutger Vandelow</b>Owner / Operator</div>
    <div class="where tiny">4715 Ave K 1/2<br>T 409 555 0147<br>nullemail@brindlecoatfinish.com<br>www.brindlecoatfinish.com</div>
    <svg class="swoosh" viewBox="0 0 100 12" height="8" preserveAspectRatio="none"><path d="M0 8 Q50 0 100 5 L100 12 L0 12Z" fill="var(--red)"/></svg>
  </section>

  <!-- business card: white front -->
  <section class="piece card card-front" style="left:14px;top:245px">
    <div class="brand"><span class="dot"></span>Brindlecoat Finish</div>
    <div class="services">Powder Coating · Ceramic Coating · Abrasive Blasting</div>
  </section>

  <!-- business card: red front -->
  <section class="piece card card-red" style="left:127px;top:245px">
    <div class="brand on-red"><span class="dot"></span>Brindlecoat Finish</div>
  </section>

  <!-- letterheads -->
  <section class="piece letter" style="left:264px;top:18px">
    <div class="brand"><span class="dot"></span>Brindlecoat Finish</div>
    <div class="contact tiny">4715 Ave K 1/2<br>T 409 555 0147<br>nullemail@brindlecoatfinish.com<br>www.brindlecoatfinish.com</div>
    <svg class="swoosh" viewBox="0 0 100 30" height="44" preserveAspectRatio="none">
      <path d="M0 10 Q55 -2 100 10" fill="none" stroke="var(--grey)" stroke-width=".8"/>
      <path d="M0 16 Q50 2 100 12 L100 30 L0 30Z" fill="var(--red)"/>
    </svg>
    <div class="foot">Powder Coating · Ceramic Coating · Abrasive Blasting</div>
  </section>

  <section class="piece letter" style="left:480px;top:18px">
    <div class="brand"><span class="dot"></span>Brindlecoat Finish</div>
    <div class="contact tiny">4715 Ave K 1/2<br>T 409 555 0147<br>nullemail@brindlecoatfinish.com<br>www.brindlecoatfinish.com</div>
    <svg class="swoosh" viewBox="0 0 100 30" height="44" preserveAspectRatio="none">
      <path d="M0 10 Q55 -2 100 10" fill="none" stroke="var(--grey)" stroke-width=".8"/>
      <path d="M0 16 Q50 2 100 12 L100 30 L0 30Z" fill="var(--red)"/>
    </svg>
    <div class="foot">Powder Coating · Ceramic Coating · Abrasive Blasting</div>
  </section>

  <!-- small envelopes -->
  <section class="piece env" style="left:696px;top:115px;height:74px">
    <div class="brand"><span class="dot"></span>Brindlecoat Finish</div>
    <div class="return tiny">4715 Ave K 1/2<br>www.brindlecoatfinish.com</div>
    <svg class="swoosh" viewBox="0 0 100 20" height="18" preserveAspectRatio="none">
      <path d="M0 6 Q55 -1 100 6" fill="none" stroke="var(--grey)" stroke-width=".8"/>
      <path d="M0 11 Q50 1 100 8 L100 20 L0 20Z" fill="var(--red)"/>
    </svg>
  </section>

  <section class="piece env" style="left:696px;top:228px;height:76px">
    <div class="brand"><span class="dot"></span>Brindlecoat Finish</div>
    <div class="return tiny">4715 Ave K 1/2<br>www.brindlecoatfinish.com</div>
    <svg class="swoosh" viewBox="0 0 100 20" height="24" preserveAspectRatio="none">
      <path d="M0 6 Q55 -1 100 6" fill="none" stroke="var(--grey)" stroke-width=".8"/>
      <path d="M0 11 Q50 1 100 8 L100 20 L0 20Z" fill="var(--red)"/>
    </svg>
  </section>

  <!-- DL envelopes -->
  <section class="piece dl" style="left:883px;top:58px;height:72px">
    <svg class="flap" viewBox="0 0 305 72" preserveAspectRatio="none"><path d="M0 0 H305 L152 40Z" fill="var(--black)"/></svg>
    <div class="brand" style="top:50px"><span class="dot"></span>Brindlecoat Finish</div>
  </section>

  <section class="piece dl" style="left:883px;top:142px;height:72px">
    <svg class="flap" viewBox="0 0 305 72" preserveAspectRatio="none"><path d="M0 0 H305 L152 40Z" fill="var(--red)"/></svg>
    <div class="brand" style="top:50px"><span class="dot"></span>Brindlecoat Finish</div>
  </section>

  <section class="piece dl" style="left:883px;top:222px;height:78px">
    <svg class="flap" viewBox="0 0 305 78" preserveAspectRatio="none"><path d="M0 0 L152 42 L305 0" fill="none" stroke="#d6d6d6" stroke-width="1"/></svg>
    <div class="brand" style="top:52px"><span class="dot"></span>Brindlecoat Finish</div>
  </section>

</main>
</body>
</html>
```